Reaching the Root: Reasoning in Clinical Choice-Making

I'd like a cover that looks like it would fit on the shelf next to "The Symptom Mirage" by Harold Vintner, "The Fall of Forgetting" by Carl Mortenson, "Meal Mend" by Neil Forsby, "The Energy Renewal Plan" by Owen Prichardson or "The Gland Renewal Plan" by the same or "The Cortex Renewal Plan" by the same ... either text only (with some interesting fonts that make the title stand out, and the subtitle smaller) or a relevant image, though I'm not entirely sure what that would be since this is a book about big-picture medical decision making.
Author name is Dr Miriam Oakhurst, NMD
I'll eventually request an e-book, paperback, and audio cover from the winner...

Target Market(s)

practicing physicians

Industry/Entity Type

medicine

Requirements
Must have
• look similar to other books in the genre

```html
<!DOCTYPE html>
<html lang="en">
<head>
<meta charset="utf-8">
<title>Reaching the Root: Reasoning in Clinical Choice-Making</title>
<link rel="stylesheet" href="https://fonts.googleapis.com/css2?family=Playfair+Display:wght@500;600&family=Source+Serif+4:wght@400;600&display=swap">
<style>
  :root {
    --backdrop: #9a9a9a;
    --paper: #fbfaf7;
    --navy: #0f2346;
    --green: #5e7a3a;
    --rule: #8fa072;
    --maze-tone: #e6e0d4;
  }
  html, body {
    margin: 0;
    padding: 0;
    width: 1200px;
    height: 1200px;
    overflow: hidden;
    background: var(--backdrop);
  }
  .cover {
    position: absolute;
    left: 252px;
    top: 93px;
    width: 696px;
    height: 1014px;
    background: var(--paper);
    overflow: hidden;
  }
  .endorsement {
    position: absolute;
    top: 30px;
    left: 0;
    width: 100%;
    text-align: center;
    font-family: "Source Serif 4", serif;
    font-size: 15.5px;
    line-height: 22px;
    color: var(--navy);
  }
  .divider {
    position: absolute;
    left: 0;
    width: 100%;
  }
  .divider-top { top: 92px; height: 24px; }
  .divider-mid { top: 482px; height: 14px; }
  .title {
    position: absolute;
    left: 0;
    width: 100%;
    text-align: center;
    font-family: "Playfair Display", serif;
    margin: 0;
    font-weight: 500;
  }
  .title-lead {
    top: 148px;
    font-size: 80px;
    line-height: 100px;
    letter-spacing: 1px;
    color: var(--navy);
  }
  .title-key {
    top: 240px;
    font-size: 222px;
    line-height: 240px;
    letter-spacing: 2px;
    color: var(--green);
  }
  .subtitle {
    position: absolute;
    left: 0;
    width: 100%;
    text-align: center;
    font-family: "Source Serif 4", serif;
    font-weight: 600;
    letter-spacing: 5px;
    margin: 0;
  }
  .subtitle-first { top: 506px; font-size: 35px; line-height: 44px; color: var(--navy); }
  .subtitle-second { top: 556px; font-size: 40px; line-height: 48px; color: var(--green); }
  .emblem {
    position: absolute;
    left: 93px;
    top: 617px;
    width: 270px;
    height: 270px;
  }
  .principles {
    position: absolute;
    left: 461px;
    top: 651px;
    width: 123px;
    height: 204px;
    border-top: 1px solid var(--rule);
    border-bottom: 1px solid var(--rule);
    font-family: "Source Serif 4", serif;
    font-size: 17px;
    letter-spacing: 1.5px;
    color: var(--navy);
    text-align: center;
  }
  .principles ul { list-style: none; margin: 0; padding: 18px 0 0; }
  .principles li { line-height: 20px; }
  .principles .sep {
    width: 4px; height: 4px; border-radius: 50%;
    background: var(--green);
    margin: 13px auto;
  }
  .author-band {
    position: absolute;
    left: 0;
    bottom: 0;
    width: 100%;
    height: 107px;
    background: var(--navy);
    border-top: 3px solid var(--green);
    display: flex;
    align-items: center;
    justify-content: center;
  }
  .author {
    font-family: "Source Serif 4", serif;
    font-weight: 600;
    font-size: 42px;
    color: var(--paper);
    margin: 0;
  }
</style>
</head>
<body>
  <main class="cover">
    <p class="endorsement">“A thoughtful framework for cutting through confusion<br>and making decisions that truly heal.”</p>

    <svg class="divider divider-top" viewBox="0 0 696 24" aria-hidden="false">
      <line x1="156" y1="14" x2="314" y2="14" stroke="var(--rule)" stroke-width="1.2"/>
      <line x1="375" y1="14" x2="540" y2="14" stroke="var(--rule)" stroke-width="1.2"/>
      <circle cx="344" cy="12" r="10" fill="var(--green)" role="img" aria-label="Small leaf sprig ornament"/>
    </svg>

    <h1 class="title title-lead">REACHING THE</h1>
    <h1 class="title title-key">ROOT</h1>

    <svg class="divider divider-mid" viewBox="0 0 696 14" aria-hidden="true">
      <line x1="194" y1="7" x2="335" y2="7" stroke="#c9c6bd" stroke-width="1"/>
      <line x1="360" y1="7" x2="503" y2="7" stroke="#c9c6bd" stroke-width="1"/>
      <circle cx="348" cy="7" r="2" fill="#b9b5aa"/>
    </svg>

    <h2 class="subtitle subtitle-first">REASONING IN CLINICAL</h2>
    <h2 class="subtitle subtitle-second">CHOICE-MAKING</h2>

    <svg class="emblem" viewBox="0 0 270 270" role="img" aria-label="Circular maze illustration with a green path leading to a sprouting leaf at its centre">
      <circle cx="135" cy="135" r="135" fill="var(--maze-tone)"/>
    </svg>

    <div class="principles">
      <ul>
        <li>CLARITY</li>
        <li class="sep" aria-hidden="true"></li>
        <li>CONTEXT</li>
        <li class="sep" aria-hidden="true"></li>
        <li>CAUSE</li>
        <li class="sep" aria-hidden="true"></li>
        <li>CONVICTION</li>
      </ul>
    </div>

    <footer class="author-band">
      <p class="author">Dr Miriam Oakhurst, NMD</p>
    </footer>
  </main>
</body>
</html>
```